Wealth Management Business Card

We are a professional services consulting firm that specializes in high net worth individuals over $25,000,000, executives C-suite and above, closely held businesses owners, family offices and highly compensated employees.

Our focus is on risk mitigation and tax efficient strategies. Our clients take their risk on themselves and have a proven track record generating wealth. Our directive is to preserve and protect the wealth they’ve already created.

Our company Harbridge Advisory is geared around five directives of asset protection:
1) Legal Structuring
2) Leverage & Financing
3) Risk Management - Asset Protection & Insurance, Trustee Work
4) Asset Management & Investing - Under www.qelvantcapital.com
5) Tax Efficient Strategies

Our Company Mark is a Pentagon with a key in the middle. A pentagon is the most efficient defensive structure. Each point of a pentagon is equal distance front every point . Each side provides support to another and works together, which is the key to our clients success.

Our key colors are blue, black and silver.

We ‘re located in the Pacific Northwest with bi coastal and international clients. We have fewer, higher net worth clients and provide exceptional customer service. We do not do social media.

website is www.harbridgepath.com

Target Market(s)

High End Clients

Contact Information for Business Card

extra thick

Font styles to use
Serif

Requirements
Must have
• Metalic foil for lettering.
Black Background on one side
White Background on the other
Horizontal Format Only
No Rounded corners
Not Marketing sales information on the card.
Nice to have
• imprinted texture on the card
Should not have
• lots of color

```html
<!DOCTYPE html>
<html lang="en">
<head>
<meta charset="utf-8">
<title>Harbridge Advisory – Business Card</title>
<link href="https://fonts.googleapis.com/css2?family=Cinzel:wght@400;500&display=swap" rel="stylesheet">
<style>
  :root {
    --page-top: #a9a9a9;
    --page-bottom: #ffffff;
    --card-black: #0d0e12;
    --card-black-sheen: #1d2028;
    --card-white: #fbfbfd;
    --card-white-shade: #eceef3;
    --foil-light: #f4f6fa;
    --foil-mid: #b9c0cc;
    --foil-dark: #8d96a5;
    --ink-blue: #15318a;
    --ink-black: #14161c;
    --ink-grey: #4d5564;
    --rule-dark: rgba(200, 206, 218, 0.45);
    --rule-light: rgba(21, 49, 138, 0.35);
  }
  * { box-sizing: border-box; margin: 0; padding: 0; }
  html, body {
    width: 1200px;
    height: 1200px;
    overflow: hidden;
  }
  body {
    background: linear-gradient(180deg, var(--page-top) 0%, #d6d6d6 45%, var(--page-bottom) 100%);
    font-family: "Cinzel", "Times New Roman", serif;
    display: flex;
    flex-direction: column;
    align-items: center;
    justify-content: center;
    gap: 72px;
  }
  .card {
    position: relative;
    width: 840px;
    height: 480px;
    overflow: hidden;
    box-shadow: 0 14px 26px rgba(0, 0, 0, 0.28);
  }

  /* Silver foil lettering */
  .foil {
    background: linear-gradient(100deg, var(--foil-dark) 0%, var(--foil-light) 35%, var(--foil-mid) 60%, var(--foil-light) 85%, var(--foil-dark) 100%);
    -webkit-background-clip: text;
    background-clip: text;
    color: transparent;
  }

  /* Front – black */
  .card-front {
    background:
      linear-gradient(100deg, transparent 20%, rgba(255,255,255,0.05) 27%, transparent 34%, transparent 62%, rgba(255,255,255,0.04) 70%, transparent 78%),
      linear-gradient(160deg, var(--card-black-sheen) 0%, var(--card-black) 50%, var(--card-black-sheen) 100%);
    display: flex;
    flex-direction: column;
    align-items: center;
    justify-content: center;
  }
  .brand {
    display: flex;
    flex-direction: column;
    align-items: center;
    gap: 22px;
  }
  .brand-mark {
    width: 46px;
    height: 46px;
    border: 5px solid var(--foil-mid);
  }
  .brand-name {
    font-weight: 400;
    font-size: 44px;
    letter-spacing: 0.04em;
    text-transform: uppercase;
    line-height: 1;
    white-space: nowrap;
  }
  .front-url {
    margin-top: 34px;
    font-size: 22px;
    letter-spacing: 0.18em;
    text-transform: uppercase;
  }

  /* Back – white */
  .card-back {
    background: linear-gradient(160deg, var(--card-white) 0%, var(--card-white-shade) 55%, var(--card-white) 100%);
    padding: 44px 52px;
  }
  .back-heading {
    font-weight: 400;
    font-size: 25px;
    line-height: 1.35;
    letter-spacing: 0.02em;
    text-transform: uppercase;
    color: var(--ink-blue);
    max-width: 760px;
  }
  .back-body {
    position: absolute;
    left: 52px;
    right: 40px;
    top: 150px;
    bottom: 64px;
    display: grid;
    grid-template-columns: 300px 1px 1fr;
    gap: 30px;
  }
  .back-brand {
    align-self: end;
    gap: 16px;
    padding-bottom: 8px;
  }
  .back-brand .brand-mark { width: 38px; height: 38px; border-width: 4px; border-color: var(--ink-blue); }
  .back-brand .brand-name { font-size: 26px; color: var(--ink-black); }
  .divider { background: var(--rule-light); }
  .directives {
    list-style: none;
    display: flex;
    flex-direction: column;
    gap: 13px;
    padding-top: 10px;
  }
  .directive {
    font-size: 19px;
    letter-spacing: 0.02em;
    color: var(--ink-black);
  }
  .directive-note {
    display: block;
    font-size: 11.5px;
    color: var(--ink-grey);
    margin-top: 2px;
    letter-spacing: 0.03em;
  }
  .back-contact {
    position: absolute;
    left: 52px;
    right: 52px;
    bottom: 24px;
    border-top: 1px solid var(--rule-light);
    padding-top: 10px;
    display: flex;
    justify-content: space-between;
    font-size: 13px;
    letter-spacing: 0.14em;
    text-transform: uppercase;
    color: var(--ink-blue);
  }
</style>
</head>
<body>

  <section class="card card-front" aria-label="Card front">
    <div class="brand">
      <div class="brand-mark"></div>
      <span class="brand-name foil">Harbridge Advisory</span>
    </div>
    <p class="front-url foil">www.harbridgepath.com</p>
  </section>

  <section class="card card-back" aria-label="Card back">
    <h1 class="back-heading">Our company Harbridge Advisory is geared around five directives of asset protection</h1>
    <div class="back-body">
      <div class="brand back-brand">
        <div class="brand-mark"></div>
        <span class="brand-name">Harbridge Advisory</span>
      </div>
      <div class="divider"></div>
      <ol class="directives">
        <li class="directive">1) Legal Structuring</li>
        <li class="directive">2) Leverage &amp; Financing</li>
        <li class="directive">3) Risk Management
          <span class="directive-note">(Asset Protection &amp; Insurance, Trustee Work)</span></li>
        <li class="directive">4) Asset Management &amp; Investing
          <span class="directive-note">(Under www.qelvantcapital.com)</span></li>
        <li class="directive">5) Tax Efficient Strategies</li>
      </ol>
    </div>
    <p class="back-contact"><span>www.harbridgepath.com</span><span>Pacific Northwest</span></p>
  </section>

</body>
</html>
```